Flyer for swimming pool service business

I am starting up a new pool cleaning business and I'm focusing on suburbs surrounding my suburb. So it will be a local service with fast, professional and friendly service.. I would like a Flyer of A5 size to drop into letterboxes local homes.

The business is called 'Gumleaf Spa Care'

The following is what I would like in the flyer

Pool service frustrating you?
Troubled by poor water condition?
Tired of doing it yourself?

Keep your swimming pool sparkling and safe all year round

- water testing
- pool chemistry
- chlorine levels
- Ph balance
- equipment maintenance
- algae prevention
- leaf and debris maintenance
- filter cleaning
- tile cleaning
- salt water systems
- local service
- chemicals supplied and delivered
All for the low price of $40 a month (plus chemicals)

Relax and let Gumleaf Spa Care take care of it for you.
for a one off service or a monthly service
no contracts

Contact details
Mitch - 0417 283 640
gumleafspacare@quollmail.net.au

Target Market(s)

the target market is a couples and familys 40-70 years old in a well off riverside suburb

Industry/Entity Type

Pool Service

Requirements
Must have
• Am looking to have a nice blue crystal clear water as part of the background either big or small.

Include my logo (provided) feel free to change the font of the Gumleaf Spas Care writing on it, if that suits your design
Should not have
• cartoonish or funny images

```html
<!DOCTYPE html>
<html lang="en">
<head>
<meta charset="utf-8">
<title>Gumleaf Spa Care – Flyer</title>
<link href="https://fonts.googleapis.com/css2?family=Arimo:wght@400;700&family=Ubuntu:wght@500;700&display=swap" rel="stylesheet">
<style>
  :root {
    --band-blue: #1d5fb0;
    --brand-blue: #1a5ea8;
    --sky-blue: #2aa3dc;
    --price-blue: #1c7be6;
    --ink: #1f3044;
    --grey: #5a5f66;
    --paper: #ffffff;
    --water-light: rgba(150, 205, 235, 0.28);
  }
  * { margin: 0; padding: 0; box-sizing: border-box; }
  html, body { width: 1200px; height: 850px; overflow: hidden; background: var(--paper); }
  .flyer {
    position: relative; width: 1200px; height: 850px;
    background: var(--paper); font-family: "Arimo", Arial, sans-serif; overflow: hidden;
  }
  .side-band {
    position: absolute; left: 0; top: 0; width: 173px; height: 850px;
    background: linear-gradient(90deg, #1a55a2, var(--band-blue));
    display: flex; justify-content: center; align-items: center;
  }
  .side-band__questions {
    writing-mode: vertical-rl; transform: rotate(180deg);
    color: #fff; font-weight: 700; font-size: 34px; line-height: 50px;
    text-align: center; white-space: nowrap;
  }
  .water-backdrop { position: absolute; left: 240px; top: 300px; }
  .brand {
    position: absolute; left: 487px; top: 22px; width: 425px; text-align: center;
  }
  .brand__mark {
    width: 112px; height: 112px; border-radius: 50%; margin: 0 auto 10px;
    background: var(--brand-blue);
  }
  .brand__name {
    border-top: 2px solid var(--brand-blue); border-bottom: 2px solid var(--brand-blue);
    color: var(--brand-blue); font-family: "Ubuntu", sans-serif; font-weight: 700;
    font-size: 30px; line-height: 42px;
  }
  .headline {
    position: absolute; left: 173px; right: 0; top: 232px; text-align: center;
    color: var(--sky-blue); font-family: "Ubuntu", sans-serif; font-weight: 700; font-size: 31px;
    text-shadow: 0 1px 2px rgba(0,0,0,0.15);
  }
  .services { position: absolute; top: 330px; list-style: none; }
  .services--left { left: 190px; }
  .services--right { left: 782px; }
  .services li {
    display: flex; align-items: center; height: 40.5px;
    color: var(--brand-blue); font-size: 31px;
  }
  .services li::before {
    content: ""; width: 22px; height: 15px; margin-right: 10px; border-radius: 50%;
    background: radial-gradient(ellipse at 50% 30%, #bfe6fb 20%, var(--sky-blue) 55%, #14508f 100%);
  }
  .price {
    position: absolute; left: 173px; right: 0; top: 620px; padding-right: 120px; text-align: center;
    color: var(--price-blue); font-weight: 700; font-size: 32px;
  }
  .details {
    position: absolute; left: 364px; width: 600px; top: 672px; text-align: center;
    color: var(--ink); font-size: 21px; line-height: 27px;
  }
  .contact {
    position: absolute; top: 790px; left: 220px; right: 40px;
    display: flex; align-items: center; color: var(--grey); font-weight: 700; font-size: 25px;
  }
  .contact__phone { display: flex; align-items: center; gap: 10px; }
  .contact__email { display: flex; align-items: center; gap: 14px; margin-left: auto; margin-right: 14px; }
</style>
</head>
<body>
<div class="flyer">
  <svg class="water-backdrop" width="940" height="420" viewBox="0 0 940 420" role="img" aria-label="Soft crystal clear pool water backdrop">
    <defs>
      <radialGradient id="waterGlow" cx="50%" cy="50%" r="50%">
        <stop offset="0%" stop-color="#9fd3ef" stop-opacity="0.35"/>
        <stop offset="100%" stop-color="#9fd3ef" stop-opacity="0"/>
      </radialGradient>
    </defs>
    <ellipse cx="470" cy="210" rx="470" ry="210" fill="url(#waterGlow)"/>
  </svg>

  <aside class="side-band">
    <p class="side-band__questions">Pool service frustrating you?<br>Troubled by poor water condition?<br>Tired of doing it yourself?</p>
  </aside>

  <header class="brand">
    <div class="brand__mark"></div>
    <div class="brand__name">Gumleaf Spa Care</div>
  </header>

  <h1 class="headline">Keep your swimming pool sparkling and safe all year round</h1>

  <ul class="services services--left">
    <li>leaf and debris maintenance</li>
    <li>filter cleaning</li>
    <li>tile cleaning</li>
    <li>salt water systems</li>
    <li>local service</li>
    <li>chemicals supplied and delivered</li>
  </ul>
  <ul class="services services--right">
    <li>water testing</li>
    <li>pool chemistry</li>
    <li>chlorine levels</li>
    <li>Ph balance</li>
    <li>equipment maintenance</li>
    <li>algae prevention</li>
  </ul>

  <p class="price">All for the low price of $40 a month (plus chemicals)</p>

  <p class="details">Relax and let Gumleaf Spa Care take care of it for you.<br>for a one off service or a monthly service<br>no contracts</p>

  <footer class="contact">
    <span class="contact__phone">Mitch
      <svg width="16" height="34" viewBox="0 0 16 34" aria-hidden="true">
        <rect x="1" y="1" width="14" height="32" rx="3" fill="#2a8fd4"/>
        <rect x="3.5" y="5" width="9" height="12" fill="#d6efff"/>
        <circle cx="8" cy="26" r="2.5" fill="#d6efff"/>
      </svg>
      0417 283 640</span>
    <span class="contact__email">
      <svg width="38" height="26" viewBox="0 0 38 26" aria-hidden="true">
        <rect x="1" y="1" width="36" height="24" rx="2" fill="#2a8fd4"/>
        <path d="M2 3 L19 15 L36 3" fill="none" stroke="#fff" stroke-width="2"/>
      </svg>
      gumleafspacare@quollmail.net.au</span>
  </footer>
</div>
</body>
</html>
```